Landing Page Design für Strategieberatung
Zielgruppe
Strategieberatung, genaue Formulierung:
KRANEX helps to identify trends, anticipate their effects and develop implementation strategies.
Aufgabenstellung
Das Design sollte schlicht und schnörkellos sein. Weitere Angaben im Briefingdokument.

```html
<!DOCTYPE html>
<html lang="en">
<head>
<meta charset="utf-8">
<title>KRANEX – Strategy Consulting</title>
<link href="https://fonts.googleapis.com/css2?family=Montserrat:wght@400;500;600;800;900&display=swap" rel="stylesheet">
<style>
  :root {
    --grey-top: #5a5a5a;
    --grey-dark: #3d3d3d;
    --grey-foot: #555555;
    --yellow: #ffc200;
    --ink: #111111;
    --text: #222222;
    --muted: #6b6b6b;
    --panel: #f4f4f4;
    --white: #ffffff;
  }
  * { margin: 0; padding: 0; box-sizing: border-box; }
  html, body { width: 1200px; height: 2717px; overflow: hidden; }
  body { position: relative; background: var(--white); font-family: "Montserrat", sans-serif; color: var(--text); }
  .abs { position: absolute; }

  .brand { font-family: "Montserrat", sans-serif; font-weight: 900; letter-spacing: 1px; color: var(--ink); font-size: 38px; line-height: 1; }
  .brand.light { color: var(--white); }

  /* header */
  .site-header { left: 0; top: 0; width: 1200px; height: 190px; background: var(--grey-top); }
  .site-header svg { position: absolute; left: 0; top: 0; }
  .header-brand { left: 0; width: 1200px; top: 42px; text-align: center; }

  /* concept */
  .concept-title { left: 171px; top: 290px; font-weight: 900; font-size: 58px; line-height: 52px; color: var(--ink); }
  .concept-title .accent { color: var(--yellow); }
  .concept-text { left: 172px; top: 421px; width: 480px; font-size: 12px; line-height: 24px; color: #444; }
  .art { background: radial-gradient(ellipse at 50% 55%, #ececec 0%, #f6f6f6 55%, rgba(255,255,255,0) 75%); }

  /* process */
  .process { left: 0; top: 751px; width: 1200px; height: 399px; background: var(--grey-dark); }
  .process-title { left: 0; top: 797px; width: 1200px; text-align: center; color: var(--white); font-weight: 900; font-size: 28px; }
  .step-art { background: radial-gradient(ellipse at 50% 50%, #8a8a8a 0%, #5a5a5a 55%, rgba(61,61,61,0) 75%); }
  .connector { height: 5px; }
  .connector.yellow { background: var(--yellow); }
  .connector.grey { background: #cfcfcf; }
  .step-label { color: #e6e6e6; font-size: 16px; line-height: 24px; text-align: center; width: 260px; }
  .step-label strong { color: var(--yellow); font-weight: 800; }

  /* why us */
  .texture { background: linear-gradient(160deg, rgba(235,235,235,0) 0%, rgba(235,235,235,0.55) 50%, rgba(235,235,235,0) 100%); }
  .why-title { left: 172px; top: 1195px; font-weight: 900; font-size: 58px; line-height: 70px; color: var(--ink); }
  .why-title .accent { color: var(--yellow); }
  .why-text { left: 173px; top: 1278px; width: 700px; font-size: 16px; line-height: 24px; color: var(--text); }
  .why-text p { margin-bottom: 24px; }

  /* chart */
  .chart-panel { left: 218px; top: 1780px; width: 674px; height: 418px; background: var(--panel); }
  .badge-ring { left: 690px; top: 1678px; width: 276px; height: 276px; border-radius: 50%; background: var(--white); }
  .badge { left: 715px; top: 1703px; width: 226px; height: 226px; border-radius: 50%; background: var(--grey-top); display: flex; align-items: center; justify-content: center; }
  .axis-label { font-weight: 600; color: var(--muted); font-size: 16px; }
  .axis-y-label { left: 80px; top: 1970px; transform: rotate(-90deg); transform-origin: center; width: 200px; text-align: center; }
  .checklist { list-style: none; font-size: 16px; line-height: 24px; color: #333; }
  .checklist li { position: relative; padding-left: 30px; margin-bottom: 24px; }
  .checklist li svg { position: absolute; left: 0; top: 7px; }

  /* footer */
  .site-footer { left: 0; top: 2295px; width: 1200px; height: 422px; background: var(--grey-foot); }
  .site-footer svg.edge { position: absolute; left: 0; top: 0; }
  .cta-title { left: 0; top: 2410px; width: 1200px; text-align: center; color: var(--white); font-weight: 800; font-size: 28px; }
  .cta-title .accent { color: var(--yellow); }
  .field { top: 2470px; height: 40px; width: 300px; background: var(--white); padding-left: 16px; font-size: 12px; color: #999; display: flex; align-items: center; }
  .submit { left: 843px; top: 2470px; width: 149px; height: 40px; background: #000; color: var(--white); font-size: 13px; display: flex; align-items: center; justify-content: center; }
  .footer-brand { left: 0; width: 1200px; top: 2596px; text-align: center; }
  .copyright { left: 0; width: 1200px; top: 2664px; text-align: center; color: var(--white); font-size: 11px; }
</style>
</head>
<body>

<header class="abs site-header">
  <svg width="1200" height="190" viewBox="0 0 1200 190">
    <polygon points="0,177 224,102 1133,158 1200,150 1200,190 0,190" fill="#ffffff"/>
  </svg>
</header>
<div class="abs header-brand"><span class="brand">KRANEX</span></div>

<section>
  <h1 class="abs concept-title">OUR<br><span class="accent">CONCEPT</span></h1>
  <p class="abs concept-text">All major strategic decisions are based on a number of factors. These are, first, an understanding of well-known trends; second, the notion that these trends will change the way a company or industry works; and third, the company’s ability to adapt to this new reality.</p>
  <div class="abs art" style="left:370px; top:595px; width:128px; height:156px;" role="img" aria-label="Line illustration of fluttering flags"></div>
  <div class="abs art" style="left:520px; top:495px; width:228px; height:256px;" role="img" aria-label="Line illustration of a flag on a puzzle piece"></div>
  <div class="abs art" style="left:740px; top:245px; width:400px; height:506px;" role="img" aria-label="Line illustration of a chess king bursting through shards"></div>
</section>

<section class="abs process"></section>
<h2 class="abs process-title">HOW THE PROCESS WORKS!</h2>
<div class="abs step-art" style="left:192px; top:872px; width:100px; height:142px;" role="img" aria-label="Flags icon"></div>
<div class="abs connector yellow" style="left:309px; top:928px; width:225px;"></div>
<div class="abs step-art" style="left:535px; top:878px; width:96px; height:132px;" role="img" aria-label="Flag on puzzle piece icon"></div>
<div class="abs connector grey" style="left:633px; top:981px; width:225px;"></div>
<div class="abs step-art" style="left:876px; top:862px; width:132px; height:156px;" role="img" aria-label="Chess king icon"></div>
<div class="abs step-label" style="left:114px; top:1040px;"><strong>Identify</strong> trends</div>
<div class="abs step-label" style="left:454px; top:1040px;"><strong>Anticipate</strong> their effects</div>
<div class="abs step-label" style="left:798px; top:1039px;"><strong>Develop</strong> implementation strategies</div>

<div class="abs texture" style="left:830px; top:1150px; width:370px; height:470px;" role="img" aria-label="Faint diagonal line texture"></div>
<div class="abs texture" style="left:0; top:1360px; width:210px; height:330px;" role="img" aria-label="Faint diagonal line texture"></div>

<section>
  <h2 class="abs why-title">WHY <span class="accent">US</span></h2>
  <div class="abs why-text">
    <p>KRANEX helps to identify trends, anticipate their effects and develop implementation strategies.</p>
    <p>KRANEX's team has a large and longstanding experience in the<br>implementation of modern forms of strategy.</p>
    <p>Our consulting services are at C-level and we have experience in the fields of fintech, biotech, energy (including the nuclear industry) and aviation.</p>
    <p>All members of KRANEX have a university degree, some of them work as lecturers at leading colleges and universities.</p>
    <p>We look forward to accompanying you in your strategic challenges.</p>
  </div>
</section>

<section>
  <div class="abs chart-panel"></div>
  <div class="abs badge-ring"></div>
  <div class="abs badge"><span class="brand light">KRANEX</span></div>
  <svg class="abs" style="left:190px; top:1738px;" width="750" height="490" viewBox="0 0 750 490" aria-hidden="true">
    <rect x="17" y="40" width="12" height="425" fill="#ffc200"/>
    <polygon points="3,44 23,0 43,44" fill="#ffc200"/>
    <rect x="17" y="453" width="690" height="12" fill="#ffc200"/>
    <polygon points="702,438 742,459 702,480" fill="#ffc200"/>
  </svg>
  <div class="abs axis-label axis-y-label">Strengths &amp; Experience</div>
  <div class="abs axis-label" style="left:776px; top:2224px;">Benefits</div>
  <ul class="abs checklist" style="left:261px; top:1820px; width:400px;">
    <li><svg width="14" height="11" viewBox="0 0 14 11"><path d="M1 5.5l4 4 8-8" fill="none" stroke="#333" stroke-width="2"/></svg>Many years of successful management experience.</li>
    <li><svg width="14" height="11" viewBox="0 0 14 11"><path d="M1 5.5l4 4 8-8" fill="none" stroke="#333" stroke-width="2"/></svg>We are living Swiss quality! Reliability. Accuracy. Punctuality. Innovation.</li>
    <li><svg width="14" height="11" viewBox="0 0 14 11"><path d="M1 5.5l4 4 8-8" fill="none" stroke="#333" stroke-width="2"/></svg>Courage for unconventional solutions.</li>
  </ul>
  <ul class="abs checklist" style="left:483px; top:2060px; width:380px;">
    <li><svg width="14" height="11" viewBox="0 0 14 11"><path d="M1 5.5l4 4 8-8" fill="none" stroke="#333" stroke-width="2"/></svg>Identify the effective challenges.</li>
    <li><svg width="14" height="11" viewBox="0 0 14 11"><path d="M1 5.5l4 4 8-8" fill="none" stroke="#333" stroke-width="2"/></svg>Development of unconventional solutions Benefits</li>
  </ul>
</section>

<footer class="abs site-footer">
  <svg class="edge" width="1200" height="100" viewBox="0 0 1200 100">
    <polygon points="0,0 1200,0 1200,5 1010,83 66,22 0,52" fill="#ffffff"/>
  </svg>
</footer>
<h2 class="abs cta-title">START WORKING WITH US <span class="accent">NOW</span></h2>
<div class="abs field" style="left:208px;">Name</div>
<div class="abs field" style="left:526px;">Phone Number</div>
<div class="abs submit">Submit</div>
<div class="abs footer-brand"><span class="brand">KRANEX</span></div>
<div class="abs copyright">© 2020 KRANEX All Rights Reserved.</div>

</body>
</html>
```